1887 Basins & Spouts Business Card

I'm wanting to get a business card designed. Our business is 1887 Basins & Spouts
Details for the card:

1887 Basins & Spouts
Name: Warren Tobbit
Email: warren@1887basinsandspouts.com.au
Website: www.1887basinsandspouts.com.au
Mobile: 0438 169 204
Phone: 02 6187 4932

Font of Basins & Spouts is called Snell Roundhand. Not sue what font logo text is.

I'm thinking two sided but it doesn't have to be.

```html
<!DOCTYPE html>
<html lang="en">
<head>
<meta charset="utf-8">
<title>1887 Basins &amp; Spouts Business Card</title>
<link href="https://fonts.googleapis.com/css2?family=Roboto:wght@400;700&display=swap" rel="stylesheet">
<style>
  :root {
    --stage: #3b3b3d;
    --card-white: #ffffff;
    --card-black: #0d0d0e;
    --pattern-a: #1c1c1e;
    --pattern-b: #111112;
    --ink: #141414;
    --ink-soft: #555555;
    --paper: #f2f2f2;
  }
  * { margin: 0; padding: 0; box-sizing: border-box; }
  html, body { width: 1200px; height: 840px; overflow: hidden; }
  body {
    background: var(--stage);
    font-family: "Roboto", sans-serif;
    position: relative;
  }
  .card {
    position: absolute;
    top: 270px;
    width: 525px;
    height: 300px;
    border-radius: 3px;
    overflow: hidden;
  }
  .card--back { left: 50px; background: var(--card-black); }
  .card--front { left: 625px; background: var(--card-white); color: var(--ink); }

  .back-pattern {
    position: absolute;
    inset: 0;
    background: radial-gradient(circle at 40% 50%, var(--pattern-a), var(--pattern-b));
  }
  .back-brand {
    position: absolute;
    top: 40px;
    right: 36px;
    display: flex;
    align-items: center;
    gap: 8px;
    color: var(--paper);
    font-size: 13px;
  }
  .brand-dot {
    width: 14px; height: 14px;
    border-radius: 50%;
    border: 1.5px solid currentColor;
  }

  .front-brand {
    position: absolute;
    top: 62px;
    left: 40px;
    display: flex;
    align-items: center;
    gap: 10px;
  }
  .front-brand .brand-dot { width: 34px; height: 34px; border-color: var(--ink); }
  .brand-name { font-size: 20px; font-weight: 400; }
  .tagline {
    position: absolute;
    top: 100px;
    left: 84px;
    font-size: 8px;
    color: var(--ink-soft);
  }

  .contacts {
    position: absolute;
    top: 150px;
    left: 232px;
    list-style: none;
    font-size: 12.5px;
    line-height: 19px;
  }
  .contacts li { display: flex; align-items: center; gap: 8px; }
  .contacts svg { width: 11px; height: 11px; flex: none; }

  .person {
    position: absolute;
    left: 40px;
    bottom: 44px;
    font-size: 22px;
    font-weight: 700;
  }
</style>
</head>
<body>
  <section class="card card--back" aria-label="Card back">
    <div class="back-pattern" role="img" aria-label="Repeating ornate frame pattern in dark grey"></div>
    <div class="back-brand"><span class="brand-dot"></span><span>1887 Basins &amp; Spouts</span></div>
  </section>

  <section class="card card--front" aria-label="Card front">
    <div class="front-brand">
      <span class="brand-dot"></span>
      <span class="brand-name">1887 Basins &amp; Spouts</span>
    </div>
    <p class="tagline">Classic style meets everyday practical use</p>

    <ul class="contacts">
      <li>
        <svg viewBox="0 0 12 12"><path d="M2.5 1h2l1 3-1.4 1a6 6 0 0 0 2.9 2.9l1-1.4 3 1v2a1 1 0 0 1-1 1A9.5 9.5 0 0 1 1.5 2a1 1 0 0 1 1-1z" fill="#141414"/></svg>
        02 6187 4932
      </li>
      <li>
        <svg viewBox="0 0 12 12"><rect x="3" y="0.8" width="6" height="10.4" rx="1" fill="none" stroke="#141414" stroke-width="1.3"/><circle cx="6" cy="9.3" r="0.7" fill="#141414"/></svg>
        0438 169 204
      </li>
      <li>
        <svg viewBox="0 0 12 12"><rect x="0.8" y="2.2" width="10.4" height="7.6" fill="#141414"/><path d="M1 2.6 6 6.6l5-4" fill="none" stroke="#fff" stroke-width="1"/></svg>
        warren@1887basinsandspouts.com.au
      </li>
      <li>
        <svg viewBox="0 0 12 12"><circle cx="6" cy="6" r="5.2" fill="#141414"/><path d="M1 6h10M6 1c-2 2.5-2 7.5 0 10M6 1c2 2.5 2 7.5 0 10" fill="none" stroke="#fff" stroke-width="0.7"/></svg>
        www.1887basinsandspouts.com.au
      </li>
    </ul>

    <h1 class="person">Warren Tobbit</h1>
  </section>
</body>
</html>
```